Social Media Post Quote #3 - Native American Organization

- RADIANT - must be included
- Protect your community. Protect Your Elders. Stay Vaccinated. must be included
- Attached, company Logo, campaign logos and sample flu social media image. - our audience likes BRIGHT colors.
- Must include image from the United States, representing Land/Nature from one of the following regions, Plains and Woodlands, or Southwest, or Mountains, or Coast.
- must include quote: The well-being of our community’s mind, body, and spirit is sacred.
- One image will be provided three times - incorporating campaign logos - in some fashion
- For inspiration - https://velmoranth.org/ and https://www.kindrelay.net/Velmoranth

```html
<!DOCTYPE html>
<html lang="en">
<head>
<meta charset="utf-8">
<title>RADIANT – Protect Your Elders</title>
<link rel="stylesheet" href="https://fonts.googleapis.com/css2?family=Barlow+Condensed:wght@500;600;700&family=Barlow:wght@400&family=Roboto+Slab:wght@500&display=swap">
<style>
  :root {
    --teal: #3f9a9b;
    --teal-light: #5bb0ae;
    --terracotta: #a34b3e;
    --cream: #f6efe3;
    --white: #ffffff;
    --quote-fill: rgba(96, 66, 50, 0.62);
    --sky-top: #c9cdd0;
    --sky-warm: #f3c77a;
    --sun: #fff6d8;
    --land-mid: #8a5a32;
    --land-dark: #3b2618;
  }
  * { margin: 0; padding: 0; box-sizing: border-box; }
  html, body { width: 1200px; height: 1196px; overflow: hidden; background: var(--white); }

  .post { position: relative; width: 1200px; height: 1196px; overflow: hidden; }

  .border-band {
    position: absolute; inset: 0;
    background: linear-gradient(135deg, var(--teal-light) 0%, #c98a78 50%, var(--teal-light) 100%);
  }
  .border-rim { position: absolute; inset: 36px; background: var(--white); }

  .landscape {
    position: absolute; left: 41px; top: 41px; width: 1118px; height: 1114px;
    background:
      radial-gradient(circle at 59% 30%, var(--sun) 0%, rgba(255,230,170,0.85) 8%, rgba(243,199,122,0.45) 24%, rgba(243,199,122,0) 46%),
      linear-gradient(180deg, var(--sky-top) 0%, #ddd3c2 22%, var(--sky-warm) 40%, #d69a55 52%, var(--land-mid) 64%, #6a4426 78%, var(--land-dark) 100%);
  }

  .campaign-badge {
    position: absolute; left: 75px; top: 93px; width: 417px; height: 117px;
    background: var(--cream);
    border: 4px solid var(--terracotta);
  }
  .campaign-badge::after {
    content: ""; position: absolute; inset: 4px; border: 1.5px solid var(--terracotta); pointer-events: none;
  }
  .campaign-name {
    position: absolute; left: 0; right: 0; top: 2px; text-align: center;
    font-family: "Barlow Condensed", sans-serif; font-weight: 700;
    font-size: 72px; letter-spacing: 3px; line-height: 80px; color: var(--teal);
  }
  .campaign-tagline {
    position: absolute; left: 8px; right: 8px; bottom: 8px; height: 24px;
    background: var(--terracotta); color: var(--white);
    font-family: "Roboto Slab", serif; font-weight: 500;
    font-size: 13px; letter-spacing: 0.6px; line-height: 24px; text-align: center; text-transform: uppercase;
  }

  .headline-steps { position: absolute; left: 0; top: 0; width: 1200px; height: 480px; overflow: visible; }

  .headline {
    position: absolute; left: 92px; top: 252px;
    font-family: "Barlow Condensed", sans-serif; font-weight: 500;
    font-size: 49px; line-height: 66px; color: var(--white); text-transform: uppercase; letter-spacing: 0.3px;
  }
  .headline strong { font-weight: 700; }

  .org-mark {
    position: absolute; left: 918px; top: 96px; width: 215px;
    display: flex; flex-direction: column; align-items: center; gap: 10px;
    font-family: "Barlow Condensed", sans-serif; font-weight: 600; color: var(--teal);
  }
  .org-mark-dot { width: 70px; height: 70px; border-radius: 50%; background: var(--teal); }
  .org-mark-name { font-size: 19px; line-height: 22px; text-align: center; text-transform: uppercase; letter-spacing: 0.4px; }

  .quote-card {
    position: absolute; left: 235px; top: 573px; width: 728px; height: 372px;
    background: var(--quote-fill);
    border: 2px solid rgba(255,255,255,0.9);
    border-top: none;
  }
  .quote-rule { position: absolute; top: 573px; height: 2px; background: var(--white); }
  .quote-rule.left { left: 235px; width: 286px; }
  .quote-rule.right { left: 680px; width: 283px; }
  .quote-mark {
    position: absolute; left: 530px; top: 470px; width: 140px; text-align: center;
    font-family: "Barlow", sans-serif; font-weight: 400; font-size: 230px; line-height: 230px; color: var(--white);
  }
  .quote-text {
    position: absolute; left: 0; right: 0; top: 84px; text-align: center;
    font-family: "Barlow", sans-serif; font-weight: 400; font-size: 52px; line-height: 70px; color: var(--white);
    letter-spacing: -0.3px;
  }
</style>
</head>
<body>
<main class="post">
  <div class="border-band" role="img" aria-label="Woven chevron border in teal and terracotta framing the post"></div>
  <div class="border-rim"></div>
  <div class="landscape" role="img" aria-label="Southwest desert mountains with saguaro cacti at golden sunset"></div>

  <div class="campaign-badge">
    <div class="campaign-name">RADIANT</div>
    <div class="campaign-tagline">COVID-19 &amp; Flu Vaccination Campaign</div>
  </div>

  <svg class="headline-steps" viewBox="0 0 1200 480" aria-hidden="true">
    <path d="M86 462 H574 V396 H657 V330 H736 V262" fill="none" stroke="#f6efe3" stroke-width="3"/>
    <path d="M90 468 H580 V402 H663 V336 H742 V266" fill="none" stroke="#3f9a9b" stroke-width="6"/>
    <path d="M78 252 H724 V318 H645 V384 H562 V450 H78 Z" fill="#a34b3e"/>
  </svg>
  <h1 class="headline">
    <strong>Protect</strong> your community.<br>
    <strong>Protect</strong> your elders.<br>
    <strong>Stay</strong> vaccinated.
  </h1>

  <div class="org-mark">
    <span class="org-mark-dot"></span>
    <span class="org-mark-name">Velmoranth Elder<br>Wellness Circle</span>
  </div>

  <div class="quote-card">
    <p class="quote-text">The well-being of our<br>community’s mind, body,<br>and spirit is sacred.</p>
  </div>
  <span class="quote-rule left"></span>
  <span class="quote-rule right"></span>
  <div class="quote-mark" aria-hidden="true">“</div>
</main>
</body>
</html>
```